Builder and developer needs website

I am re-establishing my building company after 15 years of managing other peoples building companies.
My main focus is building medium density housing with other investors as part of a syndicate. My current website is hopeless and cant be found by Google or Yahoo. It is www.dunmorebuildgroup.net.au

I have a couple of websites that I have seen that are a good inspiration for me.

I have looked at the Telvor Developments site http://www.telvor.com.au/ and like what I see. They offer the same development service that I want to offer. I also want to have a membership page/area for trades.
• The site is not wordy. It is glam and emotive
• The links to each page are easy to see and follow.
• The home page has the large images at the bottom that direct you into the emotional areas i.e. what we are building, discover the possibilities and expression of interest.
• The “Services” page is great. No long stories. Just click on the image you want to read about and off you go.
• There are a few links that don’t direct you to the correct pages i.e. expression of interest.
• There are a few places where they capture your contact details.

Also the property strategies page http://www.yieldpathways.net/bright-yield-pathways of the BYP site is very relevant to my goals. This site has a similar message but is far wordier explaining it. The research part of me likes this site as it explains more. It also uses emotive description.
The one annoying thing is the “Holdings Accelerant” sends you to a page with no tabs above to move to another page and “Estate Inner Circle” sends you to another site. I suppose his aim is to get paying people to his education courses and into his syndicates.

There is also Darryl Pendleby’s site http://darrylpendlebyestates.com.au/services/ It is hard to read due to the colours. Again it is wordy, but it is educational.

My preference is using the template of the Telvor “services” page and each wordy piece is a link.
Updates

Hello Contestants

My old website was for my old profile as a builder only. Now I want to be seen as a builder and developer as per the Telvor web site. I will be developing property just like that site and the BYP site and the Darryl Pendleby site. Thanks

Regards
Nigel Forster

Target Market(s)

Target market is people that want an investment property portfolio.
Have a SMSF or Self Managed Super Fund and want property to diversify their portfolio.
People wanting to aim for early retirement and spending time with family or working for worthwhile causes.
Have a reasonable risk profile.
Have imagination and can see how a syndicate works and the benefits for everyone.
Have imagination and can picture the finished product.
Prefer not to pay retail for property.
Prepared to wait for units to be constructed.
People that want others/joint partners around them to be come wealthy as well.

Industry/Entity Type

Education

Requirements
Nice to have
• Clear and easy navigation of the web site.
The site will be used by people in their late 30's upwards.
Sophistication
Easy maintenance of the site by me. I have limited skills in this department.
Easy SEO finding as my current site is hopeless
A members page for investors
A way of getting emails for a data base.
Should not have
• Flashing lights.
Spelling errors.
Loud noises
Background that makes the text difficult to read.

```html
<!DOCTYPE html>
<html lang="en">
<head>
<meta charset="utf-8">
<title>Dunmore Constructions – Home</title>
<link rel="stylesheet" href="https://fonts.googleapis.com/css2?family=Open+Sans:wght@300;400;600;700&display=swap">
<style>
  :root {
    --brand-blue: #1368b3;
    --header-top: #2b8ed6;
    --header-bottom: #0b5fae;
    --nav-blue: #0e5ea8;
    --accent-blue: #1487cf;
    --heading-grey: #555a5e;
    --text-grey: #555;
    --muted-grey: #7b7f82;
    --line-grey: #dcdcdc;
    --footer-bg: #f5f5f5;
    --white: #fff;
  }
  * { box-sizing: border-box; margin: 0; padding: 0; }
  html, body { width: 1050px; height: 1200px; overflow: hidden; }
  body {
    position: relative;
    background: var(--white);
    font-family: "Open Sans", Arial, sans-serif;
    color: var(--text-grey);
  }
  .abs { position: absolute; }

  /* Header */
  .top-band {
    left: 0; top: 0; width: 1050px; height: 60px;
    background: linear-gradient(var(--header-top), var(--header-bottom));
  }
  .brand-box {
    left: 53px; top: 0; width: 263px; height: 103px;
    background: var(--white);
    box-shadow: 0 2px 6px rgba(0,0,0,.12);
    display: flex; align-items: center; gap: 10px;
    padding-left: 24px;
  }
  .brand-mark { width: 26px; height: 26px; background: var(--brand-blue); }
  .brand-name { color: var(--brand-blue); font-weight: 700; line-height: 1; }
  .brand-name .big { display: block; font-size: 33px; letter-spacing: -.5px; }
  .brand-name .small { display: block; font-size: 11px; letter-spacing: 3.6px; margin-top: 5px; }

  .social { left: 735px; top: 19px; display: flex; gap: 5px; }
  .social span { width: 22px; height: 22px; border-radius: 50%; background: var(--white); }

  .phone {
    left: 834px; top: 15px; display: flex; align-items: center; gap: 6px;
    color: var(--white); font-size: 20px; font-weight: 400;
  }

  .main-nav {
    left: 387px; top: 80px; width: 597px;
    display: flex; justify-content: space-between;
    font-size: 15px; font-weight: 600; color: var(--nav-blue); text-transform: uppercase;
  }

  /* Hero */
  .hero {
    left: 53px; top: 119px; width: 945px; height: 386px;
    background: linear-gradient(100deg, #c9d8e6 0%, #9fb4c7 35%, #c5cf8e 55%, #d3dde8 75%, #6f9fcf 100%);
    border: 1px solid #cfd6dc;
    box-shadow: 0 6px 14px rgba(0,0,0,.08);
  }
  .hero-dots { left: 494px; top: 481px; display: flex; gap: 4px; }
  .hero-dots span { width: 13px; height: 13px; border-radius: 50%; background: rgba(255,255,255,.75); }

  /* Welcome */
  .welcome { left: 54px; top: 530px; width: 640px; }
  .welcome h1 { font-size: 29px; font-weight: 400; color: var(--heading-grey); line-height: 40px; white-space: nowrap; }
  .welcome .lead { font-size: 15px; margin-top: 5px; color: var(--text-grey); }
  .welcome p.body { font-size: 11px; line-height: 20px; margin-top: 10px; color: var(--text-grey); }
  .welcome p.body + p.body { margin-top: 8px; }

  /* Newsletter */
  .newsletter { left: 722px; top: 531px; width: 276px; }
  .newsletter h2 {
    font-size: 26px; font-weight: 400; color: var(--accent-blue);
    line-height: 40px; white-space: nowrap; letter-spacing: -.2px;
  }
  .newsletter p { font-size: 12px; line-height: 18px; color: var(--muted-grey); margin-top: 6px; }
  .email-field {
    margin-top: 10px; width: 276px; height: 33px;
    border: 1px solid #c9c9c9; background: #f7f7f7;
    font-size: 12px; color: var(--text-grey); padding: 7px 12px;
  }
  .subscribe-btn {
    margin: 10px 0 0 4px; width: 126px; height: 38px;
    background: linear-gradient(#20aef0, #0a7dd0);
    border-radius: 3px; color: var(--white);
    font-size: 15px; font-weight: 600; text-align: center; line-height: 38px;
  }

  /* Feature band */
  .feature-band {
    left: 0; top: 757px; width: 1050px; height: 340px;
    background: linear-gradient(#f3f3f3, #ffffff 70px);
  }
  .feature-card {
    top: 791px; width: 302px; height: 260px;
    background: linear-gradient(#ffffff 60%, #f4f4f4);
    border: 1px solid #e0e0e0;
    box-shadow: 0 1px 3px rgba(0,0,0,.08);
  }
  .feature-card .photo { height: 144px; }
  .feature-card h3 {
    font-size: 21px; font-weight: 400; color: var(--accent-blue);
    margin: 11px 0 0 16px; line-height: 28px;
  }
  .feature-card p {
    font-size: 12px; line-height: 19px; color: var(--muted-grey);
    margin: 2px 16px 0 18px;
  }
  .feature-card .more {
    display: flex; align-items: center; gap: 5px;
    font-size: 12px; font-weight: 600; color: #444;
    margin: 4px 0 0 19px; text-transform: uppercase;
  }
  .card-start { left: 53px; }
  .card-start .photo { background: linear-gradient(120deg, #9fb6cf, #d8c9b0 50%, #6f8aa6); }
  .card-services { left: 374px; }
  .card-services .photo { background: linear-gradient(120deg, #b79a6e, #7d8fa8 50%, #8a6c48); }
  .card-contact { left: 695px; }
  .card-contact .photo { background: linear-gradient(120deg, #e8e4dd, #b98d6b 50%, #ddd6cc); }

  /* Footer */
  .site-footer {
    left: 0; top: 1098px; width: 1050px; height: 102px;
    background: var(--footer-bg); border-top: 1px solid var(--line-grey);
  }
  .footer-nav {
    left: 54px; top: 1130px; font-size: 13px; color: #444; text-transform: uppercase;
    display: flex; gap: 8px;
  }
  .footer-nav .sep { color: #888; }
  .copyright { left: 57px; top: 1160px; font-size: 12px; color: var(--muted-grey); }
  .member-badge {
    left: 745px; top: 1121px; width: 243px; height: 51px;
    background: #dfe4e1; border-radius: 6px;
  }
</style>
</head>
<body>

  <header>
    <div class="abs top-band"></div>
    <div class="abs brand-box">
      <span class="brand-mark"></span>
      <span class="brand-name"><span class="big">Dunmore</span><span class="small">CONSTRUCTIONS</span></span>
    </div>
    <div class="abs social" aria-label="Social links"><span></span><span></span><span></span></div>
    <div class="abs phone">
      <svg width="24" height="24" viewBox="0 0 24 24" aria-hidden="true">
        <path d="M6 3l3 4-2 2c1 3 4 6 7 7l2-2 4 3-2 4C10 21 3 14 2 5z" fill="#fff"/>
      </svg>
      <span>0491 570 156</span>
    </div>
    <nav class="abs main-nav">
      <span>Home</span><span>About Us</span><span>Services</span><span>Getting Started</span><span>Gallery</span><span>Contact</span>
    </nav>
  </header>

  <section>
    <div class="abs hero" role="img" aria-label="Two builders in hard hats and high-visibility vests reviewing plans on a tablet in front of construction cranes"></div>
    <div class="abs hero-dots"><span></span><span></span><span></span><span></span></div>
  </section>

  <section class="abs welcome">
    <h1>Welcome to Our Website Mainpage</h1>
    <p class="lead">Phasellus felis dolor scelerisque a tempus eget lobortis id libero Aliquam nec</p>
    <p class="body">erat at purus cursus interdum Vestibulum ligula augue bibendum accumsan vestibulum ut commodo a mi Morbi ornare gravida elit Integer congue augue et malesuada iaculis ipsum dui aliquet felis at cursus magna nisl nec elit Vestibulum gravida Praesent elementum elit at tellus</p>
    <p class="body">Pellentesque faucibus Ut accumsan ultricies elit Maecenas at justo id velit placerat molestie Donec dictum lectus non odio Cras a ante vitae enim iaculis aliquam Mauris nunc quam venenatis nec euismod sit amet egest</p>
  </section>

  <aside class="abs newsletter">
    <h2>Newsletter Subscribe</h2>
    <p>Morbi ornare gravida elit Integer congue augue et malesuada iaculis ipsum dui aliq</p>
    <div class="email-field">Email address</div>
    <div class="subscribe-btn">SUBSCRIBE</div>
  </aside>

  <section>
    <div class="abs feature-band"></div>

    <article class="abs feature-card card-start">
      <div class="photo" role="img" aria-label="Business handshake beside a yellow hard hat"></div>
      <h3>Getting Started</h3>
      <p>Donec dictum lectus non odio Cras a ante vitae enim iaculis aliquam Mauris nunc quam</p>
      <span class="more">Read More <svg width="5" height="8" viewBox="0 0 5 8"><path d="M0 0l5 4-5 4z" fill="#444"/></svg></span>
    </article>

    <article class="abs feature-card card-services">
      <div class="photo" role="img" aria-label="Two tradesmen in hard hats working on site"></div>
      <h3>Services Provide</h3>
      <p>Donec dictum lectus non odio Cras a ante vitae enim iaculis aliquam Mauris nunc quam</p>
      <span class="more">Read More <svg width="5" height="8" viewBox="0 0 5 8"><path d="M0 0l5 4-5 4z" fill="#444"/></svg></span>
    </article>

    <article class="abs feature-card card-contact">
      <div class="photo" role="img" aria-label="Cutaway model of a furnished home over architectural plans"></div>
      <h3>Contact Us</h3>
      <p>Donec dictum lectus non odio Cras a ante vitae enim iaculis aliquam Mauris nunc quam</p>
      <span class="more">Read More <svg width="5" height="8" viewBox="0 0 5 8"><path d="M0 0l5 4-5 4z" fill="#444"/></svg></span>
    </article>
  </section>

  <footer>
    <div class="abs site-footer"></div>
    <nav class="abs footer-nav">
      <span>Home</span><span class="sep">|</span><span>About Us</span><span class="sep">|</span><span>Services</span><span class="sep">|</span><span>Getting Started</span><span class="sep">|</span><span>Gallery</span><span class="sep">|</span><span>Contact</span>
    </nav>
    <div class="abs copyright">© 2014 Company Name &nbsp;All right reserved &nbsp;Term of Use</div>
    <div class="abs member-badge" role="img" aria-label="Industry association membership badge"></div>
  </footer>

</body>
</html>
```